Visitenkarten-Design für Fotografen
Zielgruppe
German:
Hey,
ich habe ein Einzelunternehmen, noch im Nebengewerbe, im Bereich der professionellen Motorrad- & vor allem Autofotografie.
Nun möchte ich aber mich dieses Jahr sehr auf die Fotografie konzentrieren und benötige daher schöne, moderne Visitenkarten passend zu meiner Arbeit. Dabei möchte ich dieses Jahr auch noch zur Videografie, in Bezug auf Videos zu schönen Autos, finden und diese in mein Unternehmen mit einfließen lassen.
Hauptsächlich möchte ich mich dabei auf Sportwagen wie Varentelli, Korva GT, Halvek uvm. konzentrieren. Dabei sind die meisten Kunden halt Privatpersonen, wobei ich in Zukunft auch sehr gerne mit Firmen zusammen arbeiten möchte.
Außerdem bin ich auch oft auf Tuning Treffen in ganz Deutschland anzutreffen, komme aber aus Templin, Brandenburg.
English:
I have a sole proprietorship, still in the ancillary trade, in the field of professional motorcycle & especially car photography.
But now I want to focus very much on photography this year and therefore I need beautiful, modern business cards to match my work. This year I also want to find out about videography, in relation to videos about beautiful cars, and incorporate it into my company.
Mainly I want to focus on sports cars like Varentelli, Korva GT, Halvek and much more. Most of the customers are private individuals, although I would also like to work with companies in the future.
I am also often present at tuning meetings all over Germany, but I come from Templin, Brandenburg.
Aufgabenstellung
Visitenkarten, die
- modern
- elegant
-zweiseitig
- nicht zu überladen, aber: Picturo, Telefonnummer, Website und Mail sollten drauf sein
- ein Bezug zur Auto / Motorradfotografie sollte da sein, Schwerpunkt ist zu 80% die Auto Fotografie
- two-sided
- not to overload, but: Picturo, phone number, website and mail should be on it, further you're welcome
- a reference to car / motorcycle photography should be there, focus is 80% on car photography
Telefon: 0152 / 38170465
Website: http://lichtwerkbilder-beispiel.com (at the moment http://tobiasreuter.seitenbau-beispiel.com/lichtwerkbilder)
Mail: lichtwerk.bilder@postfach-beispiel.de

```html
<!DOCTYPE html>
<html lang="de">
<head>
<meta charset="utf-8">
<title>LichtwerkBilder – Visitenkarte</title>
<link rel="stylesheet" href="https://fonts.googleapis.com/css2?family=PT+Sans&family=PT+Serif:wght@700&display=swap">
<style>
  :root {
    --page: #ffffff;
    --card-dark: #1d1d1b;
    --accent-red: #e30613;
    --text-light: #ffffff;
    --rule: #bdbdbd;
  }
  html, body {
    margin: 0;
    padding: 0;
    width: 1200px;
    height: 1200px;
    overflow: hidden;
    background: var(--page);
  }
  .canvas {
    position: relative;
    width: 1200px;
    height: 1200px;
  }
  .card {
    position: absolute;
    left: 302px;
    width: 595px;
    height: 385px;
    overflow: hidden;
  }
  .card--front { top: 170px; background: #000; }
  .card--back { top: 645px; background: var(--card-dark); }

  .hero-photo {
    position: absolute;
    inset: 0;
    background:
      radial-gradient(ellipse 55% 40% at 50% 50%, rgba(210, 10, 10, 0.95) 0%, rgba(150, 0, 0, 0.85) 40%, rgba(60, 0, 0, 0) 75%),
      radial-gradient(ellipse 45% 35% at 15% 95%, #f2f2f2 0%, rgba(180, 180, 180, 0.7) 40%, rgba(0, 0, 0, 0) 80%),
      radial-gradient(ellipse 30% 20% at 90% 75%, rgba(200, 200, 210, 0.5) 0%, rgba(0, 0, 0, 0) 80%),
      #000;
  }

  .brand-name {
    position: absolute;
    right: 40px;
    top: 80px;
    margin: 0;
    font-family: "PT Serif", Georgia, serif;
    font-weight: 700;
    font-size: 22px;
    color: var(--text-light);
    letter-spacing: 0.5px;
  }

  .person-name {
    position: absolute;
    left: 41px;
    top: 68px;
    margin: 0;
    font-family: "PT Serif", Georgia, serif;
    font-weight: 700;
    font-size: 33px;
    line-height: 1;
    color: var(--text-light);
  }
  .person-role {
    position: absolute;
    left: 41px;
    top: 106px;
    margin: 0;
    font-family: "PT Sans", Arial, sans-serif;
    font-size: 17px;
    color: var(--accent-red);
  }
  .divider {
    position: absolute;
    left: 41px;
    top: 182px;
    width: 514px;
    height: 1px;
    background: var(--rule);
  }
  .contact-list {
    position: absolute;
    left: 41px;
    top: 214px;
    margin: 0;
    padding: 0;
    list-style: none;
    font-family: "PT Sans", Arial, sans-serif;
    font-size: 16px;
    line-height: 22.4px;
    color: var(--text-light);
  }
  .contact-item {
    position: relative;
    padding-left: 27px;
  }
  .contact-icon {
    position: absolute;
    left: 0;
    top: 4px;
    width: 15px;
    height: 15px;
    fill: var(--accent-red);
  }
</style>
</head>
<body>
<div class="canvas">

  <section class="card card--front">
    <div class="hero-photo" role="img" aria-label="Foto eines roten Sportwagens im Scheinwerferlicht vor schwarzem Hintergrund"></div>
    <p class="brand-name">LichtwerkBilder</p>
  </section>

  <section class="card card--back">
    <h1 class="person-name">Tobias Reuter</h1>
    <p class="person-role">Geschäftsführer</p>
    <p class="brand-name">LichtwerkBilder</p>
    <div class="divider"></div>

    <ul class="contact-list">
      <li class="contact-item">
        <svg class="contact-icon" viewBox="0 0 16 16"><path d="M8 0a5.5 5.5 0 0 0-5.5 5.5C2.5 9.5 8 16 8 16s5.5-6.5 5.5-10.5A5.5 5.5 0 0 0 8 0zm0 8a2.4 2.4 0 1 1 0-4.8A2.4 2.4 0 0 1 8 8z"/></svg>
        Musterstraße 12<br>12345 Musterstadt
      </li>
      <li class="contact-item">
        <svg class="contact-icon" viewBox="0 0 16 16"><path d="M4.5 0h7A1.5 1.5 0 0 1 13 1.5v13a1.5 1.5 0 0 1-1.5 1.5h-7A1.5 1.5 0 0 1 3 14.5v-13A1.5 1.5 0 0 1 4.5 0zM4.8 2v10.5h6.4V2zM8 13.3a.9.9 0 1 0 0 1.8.9.9 0 0 0 0-1.8z"/></svg>
        +49 0152 / 38170465
      </li>
      <li class="contact-item">
        <svg class="contact-icon" viewBox="0 0 16 16"><path d="M0 3h16v1.2L8 9 0 4.2zM0 5.8l8 4.8 8-4.8V13H0z"/></svg>
        lichtwerk.bilder@postfach-beispiel.de
      </li>
      <li class="contact-item">
        <svg class="contact-icon" viewBox="0 0 16 16"><path d="M8 0a8 8 0 1 0 0 16A8 8 0 0 0 8 0zm-1 1.2V5H4.6C5.1 3 6 1.7 7 1.2zm2 0c1 .5 1.9 1.8 2.4 3.8H9zM3.5 2.8A9 9 0 0 0 2.7 5H1.6a6.9 6.9 0 0 1 1.9-2.2zm9 0A6.9 6.9 0 0 1 14.4 5h-1.1a9 9 0 0 0-.8-2.2zM1.1 6.5h1.4a12 12 0 0 0 0 3H1.1a6.8 6.8 0 0 1 0-3zm3 0H7v3H4.1a10 10 0 0 1 0-3zm4.9 0h2.9a10 10 0 0 1 0 3H9zm4.5 0h1.4a6.8 6.8 0 0 1 0 3h-1.4a12 12 0 0 0 0-3zM1.6 11h1.1a9 9 0 0 0 .8 2.2A6.9 6.9 0 0 1 1.6 11zm3 0H7v3.8c-1-.5-1.9-1.8-2.4-3.8zM9 11h2.4c-.5 2-1.4 3.3-2.4 3.8zm4.3 0h1.1a6.9 6.9 0 0 1-1.9 2.2 9 9 0 0 0 .8-2.2z"/></svg>
        lichtwerk.bilder.com
      </li>
      <li class="contact-item">
        <svg class="contact-icon" viewBox="0 0 16 16"><rect x="1" y="1" width="14" height="14" rx="3"/></svg>
        picturo.com/lichtwerk_bilder
      </li>
    </ul>
  </section>

</div>
</body>
</html>
```